Simple 1 page layout for addrforge-tool.com

Visit http://addrforge-tool.com

The site calculates ipv6 unique local addresses for free. The content will stay as it is. There's going to be Brelvo promoslots below the red box and at the bottom of the page.

The red box contains the most important information on this page. The users focus should go there immediately.

The contents below composition is also kind of important.

Reason: I'm very busy at the moment. I need more time for evaluation and feedback. Thanks for your contributions and your patience.

Target Market(s)

IT and networking people

Industry/Entity Type

Brelvo

Requirements
Must have
• I need all pieces nicely cut, so I only have to do HTML and CSS.

```html
<!DOCTYPE html>
<html lang="en">
<head>
<meta charset="utf-8">
<title>Unique Local IPV6 – Local Network Address Generator</title>
<link rel="stylesheet" href="https://fonts.googleapis.com/css2?family=Arimo:wght@400;700&family=Open+Sans:wght@300;400&display=swap">
<style>
:root{
  --page-bg:#ffffff;
  --ink:#111111;
  --body-ink:#444444;
  --muted:#666666;
  --hero-blue:#00a0dc;
  --link-blue:#0a92c8;
  --btn-top:#14b2ea;
  --btn-bottom:#0094cf;
  --rule:#d6d6d6;
  --header-top:#ffffff;
  --header-bottom:#ececec;
  --class-red:#e0121a;
  --class-green:#22a83a;
  --social-bg:#f4f4f4;
  --social-border:#b9b9b9;
  --like-blue:#4a64a0;
  --plus-red:#d7402c;
  --mark-blue:#1e8fd8;
}
*{margin:0;padding:0;box-sizing:border-box}
html,body{width:1000px;height:1200px;overflow:hidden;background:var(--page-bg)}
body{position:relative;font-family:"Arimo",Helvetica,Arial,sans-serif;color:var(--body-ink)}
.abs{position:absolute}

/* Header bar */
.site-header{left:46px;top:18px;width:910px;height:93px;border:1px solid var(--rule);border-radius:3px;
  background:linear-gradient(var(--header-top),var(--header-bottom));box-shadow:0 1px 3px rgba(0,0,0,.12)}
.brand-dot{left:22px;top:21px;width:48px;height:48px;border-radius:50%;background:var(--mark-blue)}
.brand-name{left:93px;top:25px;font-size:18px;line-height:22px;color:#333}
.brand-name b{font-weight:700}
.brand-name .tagline{display:block;font-weight:700;font-size:18px}
.social{top:38px;height:20px;font-size:11px;line-height:18px;display:flex;gap:4px;align-items:center}
.social .pill{border:1px solid var(--social-border);background:var(--social-bg);border-radius:3px;padding:0 7px;color:#333;font-weight:700}
.social .count{border:1px solid var(--social-border);background:#fff;border-radius:2px;padding:0 7px;color:#333}
.social .like{color:var(--like-blue)}
.social .plus{color:var(--plus-red)}
.social .note{color:#555;font-size:11px;margin-left:2px}
.social .note span{color:var(--link-blue)}

/* Hero */
.hero{left:46px;top:137px;width:910px;height:187px;background:var(--hero-blue);border-radius:3px;color:#fff;
  font-family:"Open Sans",Helvetica,Arial,sans-serif;font-weight:400}
.hero-prefix{left:33px;top:16px;font-size:44px;letter-spacing:-1px;line-height:56px}
.hero-row{left:33px;font-size:22px;line-height:30px;letter-spacing:-.4px}
.hero-row .val{position:absolute;left:214px;white-space:nowrap}

/* Text blocks */
h2{font-family:"Arimo",Helvetica,Arial,sans-serif;font-weight:700;font-size:19px;color:var(--ink);letter-spacing:-.3px;line-height:24px}
.copy{font-size:13px;color:var(--body-ink)}
.col-left{left:46px;width:440px}
.col-right{left:513px;width:443px}

/* Composition table */
.bit-table{left:46px;top:388px;border-collapse:collapse;font-size:13px;color:#333}
.bit-table td{border:1px solid var(--rule);height:34px;padding:0 0 0 13px}
.bit-table tr:nth-child(1) td{background:#f7f7f7}
.bit-table tr:nth-child(2) td{text-align:right;padding:0 12px 0 0}
.field-list{left:47px;top:465px;font-size:13px;line-height:20px;display:grid;grid-template-columns:94px auto}
.field-list dt{font-weight:700;color:#222}
.field-list dd{color:#444}

/* Links */
.faq-links{list-style:none;font-size:14px;font-weight:700;line-height:25px}
.faq-links a{color:var(--link-blue)}

/* Address classes */
.addr-head{font-size:13px;font-weight:700}
.addr-head.ipv4{color:var(--class-red)}
.addr-head.ipv6{color:var(--class-green)}
.addr-grid{display:grid;grid-template-columns:93px auto;font-size:13px;line-height:19px}
.addr-grid dt{font-weight:700;color:#222}

/* Button */
.cta{left:46px;top:1115px;width:315px;height:59px;border-radius:3px;background:linear-gradient(var(--btn-top),var(--btn-bottom));
  color:#fff;font-weight:700;font-size:19px;display:flex;align-items:center;justify-content:center;text-decoration:none;letter-spacing:-.2px}
</style>
</head>
<body>

<header class="site-header abs">
  <div class="brand-dot abs"></div>
  <div class="brand-name abs">Unique Local <b>IPV6</b><span class="tagline">Local Network Address Generator</span></div>
  <div class="social abs" style="left:471px"><span class="pill like">Likewall</span><span class="count">4K</span></div>
  <div class="social abs" style="left:587px"><span class="pill">Chirp</span><span class="count">1</span></div>
  <div class="social abs" style="left:679px"><span class="pill plus">+1</span><span class="note">+1 &nbsp;Recommend this <span>on Brelvo</span></span></div>
</header>

<section class="hero abs">
  <div class="hero-prefix abs">fde5:98aa:1ace::/48</div>
  <div class="hero-row abs" style="top:69px">1st 64-bit subnet<span class="val">fde5:98aa:1ace::/64</span></div>
  <div class="hero-row abs" style="top:101px">last 64-bit subnet<span class="val">fde5:98aa:1ace:ffff::/64</span></div>
  <div class="hero-row abs" style="top:134px">Just reload this page to get a new one</div>
</section>

<h2 class="abs" style="left:46px;top:349px">Composition</h2>
<table class="bit-table abs">
  <tr><td style="width:62px">7 bits</td><td style="width:33px">1</td><td style="width:80px">40 bits</td><td style="width:88px">16 bits</td><td style="width:103px">64 bits</td></tr>
  <tr><td>Prefix</td><td>L</td><td>Global ID</td><td>Subnet ID</td><td>Interface ID</td></tr>
</table>
<dl class="field-list abs">
  <dt>Prefix</dt><dd>fc::/7</dd>
  <dt>Local (L)</dt><dd>1</dd>
  <dt>Global ID</dt><dd>e598aa1ace changes every time you visit this page</dd>
  <dt>Subnet ID</dt><dd>0 - ffff use freely for your own IPv6 subnetting</dd>
  <dt>Interface ID</dt><dd style="padding-left:14px">Your host address.</dd>
</dl>

<h2 class="abs col-right" style="top:364px">What's the use?</h2>
<ul class="faq-links abs col-right" style="top:391px">
  <li><a href="#what">What's a unique local address?</a></li>
  <li><a href="#use">What's the use?</a></li>
  <li><a href="#why">Why do they need to be unique?</a></li>
  <li><a href="#really">Are they really globally unique?</a></li>
  <li><a href="#easy">Isn't there an easy way?</a></li>
  <li><a href="#subnet">What is the subnet id?</a></li>
  <li><a href="#more">Where can I get more information?</a></li>
</ul>

<h2 id="what" class="abs col-left" style="top:593px">What's a unique local address?</h2>
<p class="copy abs col-left" style="top:620px;line-height:23px">IPv6 unique local addresses are similar to the IPv4 private address classes with one big difference: THE ARE UNIQUE.</p>
<div class="addr-head ipv4 abs" style="left:46px;top:681px">IPv4 private addresses</div>
<dl class="addr-grid copy abs" style="left:46px;top:699px">
  <dt>Class A</dt><dd>10.0.0.0/8</dd>
  <dt>Class B</dt><dd>172.16.0.0/12</dd>
  <dt>Class C</dt><dd>192.168.0.0/16</dd>
</dl>
<div class="addr-head ipv6 abs" style="left:283px;top:681px">IPv6 unique local addresses</div>
<div class="copy abs" style="left:283px;top:699px;line-height:19px">fd::/48 - fd:ffff:ffff::/48</div>

<h2 id="use" class="abs col-right" style="top:593px">What's the use?</h2>
<p class="copy abs col-right" style="top:622px;line-height:21px">Local network addresses are used to make specific services only available for people and computers within your private network. For example if your company runs an intranet website containing confidential information about products, sales, customers or what so ever. This information might be vital for your employees to do their jobs, but you definitely don't want to make this website available publicly.</p>

<h2 id="why" class="abs col-left" style="top:785px">Why do they need to be unique?</h2>
<p class="copy abs col-left" style="top:813px;line-height:21px">Sometimes you want to join two or more private networks. A common example is when you connect your PC from your home network to your office network using a VPN. When both networks use the same private address range (e.g. 192.168.1.0/24) you only reach the office network during your VPN session as a result of a routing problem.</p>

<h2 id="really" class="abs col-right" style="top:785px">Are they really globally unique?</h2>
<p class="copy abs col-right" style="top:812px;line-height:24.7px">The global id part of unique local addresses is a randomly generated 40-bit integer. So there's a small possibility that two networks on this planet use the same unique local address. But there's a very little likelihood that this is ever going to happen. PROBABILITY: 1:1099511627776 or ~0.000000000001</p>

<h2 id="easy" class="abs col-left" style="top:948px">Isn't there an easy way?</h2>
<p class="copy abs col-left" style="top:975px;line-height:24.8px">If you want to use a unique local network for your personal use or for testing only, no one bars you from using fd::/48, fd:abba::/48 or fd:1234::/48. But keep in mind there's are reason they have been made unique in the first place. And there's actually no good reason not to use a randomly generated address. How about that one on top of this page?</p>

<h2 id="subnet" class="abs col-right" style="top:948px">What is the subnet id?</h2>
<p class="copy abs col-right" style="top:975px;line-height:24.8px">After the global id you have 16 bits for your subnetting. Use them at will.<br>If you don't have any subnetting plans right now, just start with 0000 (luckily you don't have to write that).</p>

<a id="more" class="cta abs" href="http://addrforge-tool.com">Get more information Here</a>

</body>
</html>
```